BRISK GUARD WEBSITE BANNER DESIGN OF AWESOME

Please take a look at the attached Banner. I want a redesign Idea. The requirements are below.

1)Must Use Website Background
2)Must Use Photo Provided
3)Must Include Button
4)Website the banner will be used on you can see the current at the bottom of the page: https://b.plomvarn.com

Target Market(s)

Anyone Seeking Security Guard Services

```html
<!DOCTYPE html>
<html lang="en">
<head>
<meta charset="utf-8">
<title>Brisk Guard – Website Banner Concepts</title>
<link href="https://fonts.googleapis.com/css2?family=Poppins:wght@400;500;600;700&display=swap" rel="stylesheet">
<style>
  :root{
    --page-bg:#f2f2f2;
    --ink:#1a1a1a;
    --navy-dark:#17365c;
    --navy:#17497a;
    --navy-light:#1a5586;
    --orange:#f9a91a;
    --white:#ffffff;
    --cyan:#0ff0ff;
    --frame:rgba(120,170,220,.35);
  }
  *{box-sizing:border-box;margin:0;padding:0}
  html,body{width:1200px;height:901px;overflow:hidden;background:var(--page-bg);font-family:"Poppins",sans-serif}
  .board{position:relative;width:1200px;height:901px}
  .board-label{position:absolute;left:0;width:1200px;text-align:center;font-size:21px;font-weight:400;color:var(--ink);letter-spacing:.5px}
  .banner{position:absolute;left:65px;width:1067px;height:313px;overflow:hidden;
    background:
      linear-gradient(160deg,rgba(20,40,75,.55) 0%,rgba(20,40,75,.35) 28%,rgba(20,40,75,0) 29%),
      linear-gradient(115deg,var(--navy-dark) 0%,var(--navy) 45%,var(--navy-light) 100%)}
  .banner::after{content:"";position:absolute;inset:7px;border:1px solid var(--frame);pointer-events:none}
  .headline{position:absolute;left:0;width:640px;top:60px;text-align:center;font-size:44px;font-weight:700;color:var(--orange);letter-spacing:-.5px;line-height:1}
  .tagline{position:absolute;left:0;width:640px;top:108px;text-align:center;font-size:22px;font-weight:400;color:var(--white);line-height:1.3}
  .cta{position:absolute;left:239px;top:149px;width:164px;height:39px;border-radius:20px;background:var(--orange);
    color:var(--navy-dark);font-size:14px;font-weight:400;display:flex;align-items:center;justify-content:center;gap:6px;
    box-shadow:2px 3px 6px rgba(0,0,0,.35);text-decoration:none}
  .cta svg{width:20px;height:10px}
  .features{position:absolute;display:flex;align-items:center;color:var(--white)}
  .features--plain{left:66px;top:213px;font-size:12.5px;font-weight:400}
  .features--plain .feature{display:flex;align-items:center;gap:9px;padding:0 10px}
  .features--plain .feature:first-child{padding-left:0}
  .features--plain .feature + .feature{border-left:1px solid rgba(255,255,255,.45)}
  .features--plain .shield{width:27px;height:33px}
  .features--pill{left:89px;top:225px;height:32px;padding:0 12px;border:1px solid rgba(160,200,240,.45);border-radius:16px;font-size:12.5px;font-weight:600}
  .features--pill .feature{display:flex;align-items:center;gap:4px;padding:0 8px;height:26px}
  .features--pill .feature + .feature{border-left:1px solid rgba(255,255,255,.4)}
  .features--pill .shield{width:15px;height:18px}
  .hero-photo{position:absolute;left:676px;top:16px;width:256px;height:285px;filter:drop-shadow(0 0 8px var(--cyan))}
</style>
</head>
<body>
<main class="board">

  <p class="board-label" style="top:70px">Banner-1</p>
  <section class="banner" style="top:119px">
    <h1 class="headline">GET SECURED TODAY</h1>
    <p class="tagline">We take your security personal.</p>
    <a class="cta" href="https://b.plomvarn.com">GET STARTED
      <svg viewBox="0 0 20 10"><path d="M0 5H19M14 1l5 4-5 4" fill="none" stroke="currentColor" stroke-width="1.2"/></svg>
    </a>
    <ul class="features features--plain" style="list-style:none">
      <li class="feature">
        <svg class="shield" viewBox="0 0 27 33"><path d="M13.5 1.5 25 5.5v11c0 7-5 12-11.5 15C7 28.5 2 23.5 2 16.5v-11z" fill="none" stroke="var(--orange)" stroke-width="2"/><rect x="8" y="10" width="11" height="8" fill="none" stroke="var(--orange)" stroke-width="1.3"/><path d="M13.5 18v3M10 22h7" stroke="var(--orange)" stroke-width="1.3"/></svg>
        CLIENT PORTAL</li>
      <li class="feature">
        <svg class="shield" viewBox="0 0 27 33"><path d="M13.5 1.5 25 5.5v11c0 7-5 12-11.5 15C7 28.5 2 23.5 2 16.5v-11z" fill="none" stroke="var(--orange)" stroke-width="2"/><circle cx="13.5" cy="15.5" r="6" fill="none" stroke="var(--orange)" stroke-width="1.3"/><path d="M13.5 12.5v3l2 1.5" fill="none" stroke="var(--orange)" stroke-width="1.3"/></svg>
        24X7 DISPATCH</li>
      <li class="feature">
        <svg class="shield" viewBox="0 0 27 33"><path d="M13.5 1.5 25 5.5v11c0 7-5 12-11.5 15C7 28.5 2 23.5 2 16.5v-11z" fill="none" stroke="var(--orange)" stroke-width="2"/><rect x="9" y="9" width="9" height="13" fill="none" stroke="var(--orange)" stroke-width="1.3"/><path d="M11 12.5h5M11 15.5h5M11 18.5h5" stroke="var(--orange)" stroke-width="1"/></svg>
        NO BINDING CONTRACTS</li>
    </ul>
    <svg class="hero-photo" viewBox="0 0 256 285" role="img" aria-label="Photo of a security guard shining a flashlight up a stairwell, framed in a hexagon">
      <defs><linearGradient id="photo1" x1="0" y1="0" x2="0.3" y2="1"><stop offset="0" stop-color="#5b7fb0"/><stop offset=".5" stop-color="#2a3f5c"/><stop offset="1" stop-color="#0d1420"/></linearGradient></defs>
      <polygon points="128,5 251,74 251,211 128,280 5,211 5,74" fill="url(#photo1)" stroke="var(--cyan)" stroke-width="10" stroke-linejoin="round"/>
    </svg>
  </section>

  <p class="board-label" style="top:468px">Banner-2</p>
  <section class="banner" style="top:517px">
    <h1 class="headline" style="top:68px">GET SECURED TODAY</h1>
    <p class="tagline" style="top:116px;font-weight:500">We take your security personal.</p>
    <a class="cta" style="top:158px" href="https://b.plomvarn.com">GET STARTED
      <svg viewBox="0 0 20 10"><path d="M0 5H19M14 1l5 4-5 4" fill="none" stroke="currentColor" stroke-width="1.2"/></svg>
    </a>
    <ul class="features features--pill" style="list-style:none">
      <li class="feature"><svg class="shield" viewBox="0 0 15 18"><path d="M7.5 1 14 3.2v5.5c0 4-3 6.8-6.5 8.3C4 15.5 1 12.7 1 8.7V3.2z" fill="none" stroke="var(--orange)" stroke-width="1.3"/><path d="M4.5 9l2 2 4-4" fill="none" stroke="var(--orange)" stroke-width="1.3"/></svg>CLIENT PORTAL</li>
      <li class="feature"><svg class="shield" viewBox="0 0 15 18"><path d="M7.5 1 14 3.2v5.5c0 4-3 6.8-6.5 8.3C4 15.5 1 12.7 1 8.7V3.2z" fill="none" stroke="var(--orange)" stroke-width="1.3"/><path d="M4.5 9l2 2 4-4" fill="none" stroke="var(--orange)" stroke-width="1.3"/></svg>24X7 DISPATCH</li>
      <li class="feature"><svg class="shield" viewBox="0 0 15 18"><path d="M7.5 1 14 3.2v5.5c0 4-3 6.8-6.5 8.3C4 15.5 1 12.7 1 8.7V3.2z" fill="none" stroke="var(--orange)" stroke-width="1.3"/><path d="M4.5 9l2 2 4-4" fill="none" stroke="var(--orange)" stroke-width="1.3"/></svg>NO BINDING CONTRACTS</li>
    </ul>
    <svg class="hero-photo" viewBox="0 0 256 285" role="img" aria-label="Photo of a security guard shining a flashlight up a stairwell, framed in a hexagon">
      <defs><linearGradient id="photo2" x1="0" y1="0" x2="0.3" y2="1"><stop offset="0" stop-color="#5b7fb0"/><stop offset=".5" stop-color="#2a3f5c"/><stop offset="1" stop-color="#0d1420"/></linearGradient></defs>
      <polygon points="128,5 251,74 251,211 128,280 5,211 5,74" fill="url(#photo2)" stroke="var(--cyan)" stroke-width="10" stroke-linejoin="round"/>
    </svg>
  </section>

</main>
</body>
</html>
```